Flyer Design

A flyer to introduce our new business called Smilewagons on Wheels ,we are a mobile dental hygienist service based in the Teesside area of England.We use portable equipment to treat clients where they live or work Since may 2013 in the uk hygienists no longer need to work with a dentist ,therefore clients can now access dental hygiene care without seeing a dentist.We offer scale and polish ,oral hygiene advice .Our colours are pink,green and purple.we would like to stress the importance of a regular professional clean with the convenience of being treated at home

Target Market(s)

over 18 years of age who choose or need to have there scale and polish at home

Industry/Entity Type

Dental

Colors
e34297
9ccb3b
876aae

Requirements
Must have
• ,must have our logo and our contact details tel 07812460395 and email info@smilewagonsonwheels.co.uk
The hygienists names Moira Palfrey and Janet Ruddock
eye catching and colourful ,not to many words,but getting across we are for anyone who chooses or needs their treatment at home
Nice to have
• we would like the logo to be prominent ,our colours are pink ,green and purple .the font easy to read for older people
Should not have
• A lot of writing on the front the page ,

```html
<!DOCTYPE html>
<html lang="en">
<head>
<meta charset="utf-8">
<title>Smilewagons on Wheels – Mobile Dental Hygienists</title>
<link rel="stylesheet" href="https://fonts.googleapis.com/css2?family=Teko:wght@500&family=Lato:wght@400;700;900&display=swap">
<style>
  :root{
    --pink:#cf3d93;
    --green:#63bf5e;
    --text:#222;
    --muted:#5a5a5a;
    --paper:#ffffff;
    --backdrop:#2e2e2e;
  }
  *{box-sizing:border-box;margin:0;padding:0}
  html,body{width:806px;height:1200px;overflow:hidden}
  body{background:var(--backdrop);font-family:"Lato",Arial,sans-serif;color:var(--text);position:relative}
  .flyer{position:absolute;left:58px;top:108px;width:694px;height:978px;background:var(--paper);overflow:hidden}
  .flyer-shapes{position:absolute;inset:0}
  .brand{position:absolute;left:30px;top:92px;width:260px;text-align:center}
  .brand-name{font-weight:400;font-size:22px;color:var(--pink);display:block}
  .brand-dot{display:block;width:44px;height:44px;border-radius:50%;background:var(--green);margin:12px auto 14px}
  .brand-tagline{font-size:16px;color:var(--green);display:block}
  .headline{position:absolute;left:20px;top:226px;font-family:"Teko",sans-serif;font-weight:500;font-size:40px;line-height:41px;text-transform:uppercase;color:var(--green);white-space:nowrap}
  .headline .lead{color:var(--pink)}
  .intro{position:absolute;left:20px;top:358px;font-size:14px;line-height:19px;color:var(--muted)}
  .intro p:first-child{width:320px}
  .intro p+p{margin-top:8px;width:396px}
  .feature{position:absolute;top:527px;width:230px}
  .feature--care{left:17px}
  .feature--access{left:258px}
  .feature--reach{left:486px}
  .feature-head{display:flex;align-items:center;gap:6px;height:66px}
  .feature-icon{width:62px;height:62px;border-radius:50%;background:var(--green);border:3px solid #fff;box-shadow:0 0 0 2px var(--green);flex:none;display:flex;align-items:center;justify-content:center}
  .feature-title{font-family:"Teko",sans-serif;font-weight:500;font-size:21px;text-transform:uppercase;color:var(--green);white-space:nowrap}
  .feature-title .lead{color:var(--pink)}
  .feature-text{margin:10px 0 0 2px;font-size:11px;line-height:16.5px;color:var(--text);width:200px}
  .closing{position:absolute;right:20px;top:768px;width:360px;text-align:right;font-size:11px;line-height:17px}
  .contact{position:absolute;right:20px;top:845px;text-align:right;font-style:normal}
  .phone{display:flex;align-items:center;justify-content:flex-end;gap:10px;font-weight:700;font-size:29px;line-height:34px}
  .phone-icon{width:34px;height:34px;background:var(--pink);border-radius:4px;display:flex;align-items:center;justify-content:center}
  .email{display:block;margin-top:4px;font-size:17.5px}
</style>
</head>
<body>
<main class="flyer">
  <svg class="flyer-shapes" viewBox="0 0 694 978" width="694" height="978">
    <defs>
      <linearGradient id="treatment-tones" x1="0" y1="0" x2="1" y2="1">
        <stop offset="0" stop-color="#e6e9ec"/>
        <stop offset="0.5" stop-color="#d9b49a"/>
        <stop offset="1" stop-color="#7fa6b7"/>
      </linearGradient>
      <linearGradient id="chair-tones" x1="0" y1="0" x2="1" y2="1">
        <stop offset="0" stop-color="#7fb3df"/>
        <stop offset="0.6" stop-color="#e0bfa8"/>
        <stop offset="1" stop-color="#f2f2f2"/>
      </linearGradient>
    </defs>
    <rect class="band-top" x="0" y="0" width="694" height="110" fill="var(--green)"/>
    <path class="band-top-curve" d="M0,80 C150,56 300,50 440,62 L694,52 L694,978 L0,978Z" fill="var(--paper)"/>
    <path d="M0,74 C150,50 300,44 440,56" fill="none" stroke="var(--pink)" stroke-width="4"/>
    <path class="band-bottom-curve" d="M0,900 C200,912 460,930 694,890 L694,978 L0,978Z" fill="var(--green)"/>
    <path d="M0,900 C200,912 460,930 694,890" fill="none" stroke="#fff" stroke-width="10"/>
    <path d="M150,907 C300,918 480,930 694,896" fill="none" stroke="var(--pink)" stroke-width="4"/>
    <path role="img" aria-label="Photo of a patient having her teeth cleaned by a hygienist"
      d="M335,95 C325,45 370,30 420,32 C470,35 505,55 540,55 C575,55 610,28 660,28 C690,28 700,50 700,80 L700,300 C695,400 680,490 645,492 C610,494 600,420 588,380 C578,350 552,350 542,380 C530,420 520,488 480,492 C445,494 430,455 420,410 C400,330 362,262 348,192 C340,150 342,120 335,95Z"
      fill="url(#treatment-tones)" stroke="var(--pink)" stroke-width="6"/>
    <circle cx="58" cy="820" r="58" fill="var(--pink)"/>
    <circle cx="240" cy="796" r="34" fill="var(--green)"/>
    <circle cx="262" cy="858" r="44" fill="var(--pink)"/>
    <circle cx="288" cy="792" r="18" fill="var(--pink)"/>
    <circle cx="8" cy="892" r="18" fill="var(--green)"/>
    <circle cx="304" cy="910" r="16" fill="var(--green)"/>
    <circle cx="132" cy="842" r="80" fill="#fff"/>
    <circle role="img" aria-label="Photo of a smiling patient in the dental chair" cx="132" cy="842" r="74" fill="url(#chair-tones)" stroke="var(--green)" stroke-width="5"/>
  </svg>

  <div class="brand">
    <span class="brand-name">Smilewagons on Wheels</span>
    <span class="brand-dot"></span>
    <span class="brand-tagline">Mobile Dental Hygienists</span>
  </div>

  <h1 class="headline"><span class="lead">The hygienists names</span><br>Moira Palfrey and<br>Janet Ruddock</h1>

  <div class="intro">
    <p>We are a mobile dental hygienist service based in the Teesside area of England.</p>
    <p>We use portable equipment to treat clients where they live or work Since may 2013 in the uk hygienists no longer need to work with a dentist ,therefore clients can now access dental hygiene care without seeing a dentist.We offer scale and polish , oral hygiene advice .</p>
  </div>

  <article class="feature feature--care">
    <div class="feature-head">
      <span class="feature-icon"><svg width="30" height="30" viewBox="0 0 30 30"><path d="M6,15 L12,21 L24,8" fill="none" stroke="#fff" stroke-width="4" stroke-linecap="round" stroke-linejoin="round"/></svg></span>
      <h2 class="feature-title"><span class="lead">Lorem Ipsum</span> is simply</h2>
    </div>
    <p class="feature-text">Lorem Ipsum is simply dummy text of the printing and typesetting industry. Lorem Ipsum has been the industry's standard dummy text ever since the 1500s, when an unknown printer took a galley of type and scrambled it to make a type specimen book.</p>
  </article>
  <article class="feature feature--access">
    <div class="feature-head">
      <span class="feature-icon"><svg width="32" height="32" viewBox="0 0 32 32" fill="none" stroke="#fff" stroke-width="3" stroke-linecap="round"><circle cx="14" cy="4" r="2.5" fill="#fff" stroke="none"/><path d="M14,9 L14,18 L22,18 L25,26"/><path d="M10,14 A8,8 0 1 0 20,25"/></svg></span>
      <h2 class="feature-title"><span class="lead">Dummy text</span> of the</h2>
    </div>
    <p class="feature-text">Lorem Ipsum is simply dummy text of the printing and typesetting industry. Lorem Ipsum has been the industry's standard dummy text ever since the 1500s, when an unknown printer took a galley of type and scrambled it to make a type specimen book.</p>
  </article>
  <article class="feature feature--reach">
    <div class="feature-head">
      <span class="feature-icon"><svg width="32" height="32" viewBox="0 0 32 32" fill="none" stroke="#fff" stroke-width="2"><circle cx="16" cy="16" r="13"/><ellipse cx="16" cy="16" rx="6" ry="13"/><path d="M3,16 H29 M5,9 H27 M5,23 H27"/></svg></span>
      <h2 class="feature-title"><span class="lead">Printing</span> and</h2>
    </div>
    <p class="feature-text">Lorem Ipsum is simply dummy text of the printing and typesetting industry. Lorem Ipsum has been the industry's standard dummy text ever since the 1500s, when an unknown printer took a galley of type and scrambled it to make a type specimen book.</p>
  </article>

  <p class="closing">Lorem Ipsum is simply dummy text of the printing and typesetting industry. Lorem Ipsum has been the industry's standard dummy text ever since the 1500s, when an unknown printer took a galley of type and scrambled it to make a type specimen book.</p>

  <address class="contact">
    <span class="phone"><span class="phone-icon"><svg width="20" height="22" viewBox="0 0 20 22"><path d="M5,1 L8,6 L6,8 C7,11 9,14 12,16 L14,14 L19,17 L17,21 C9,20 2,12 1,4Z" fill="#fff"/></svg></span>07812460395</span>
    <span class="email">info@smilewagonsonwheels.co.uk</span>
  </address>
</main>
</body>
</html>
```